Radiant Harvest Gathering 2021

I am looking to create a flyer for a one day prayer retreat our church is organizing. This flyer will be posted on social media, websites, mobile apps, and will also be printed so it can be mailed to people.

I am looking for something professional, with good use of our logo and band colors (logo colors).

I am counting on the designer's skill, creativity, art and knowledge of media communication to produce a flyer that will effectively and quickly convey the message we are trying to spread.

CONTENT OF THE FLYER:
Event title: Radiant Harvest Gathering
Date: Tuesday July 2nd, 2021
Time: 11:00AM - 7:00PM
Bellmore Hotel, 4817 Wexley Avenue, Portland, Maine 04109 (Room: Tamarind)
Event Key words to highlight what the event is about: Prayer, Fasting, Worship, Prophecy, Revival.
Key phrases:
A one day prayer retreat.
Jesus Chris is Lord

Contact info:
www.quvello.org
Phone: 207 555 0148
Email: contact@brookmeadow.org

```html
<!DOCTYPE html>
<html lang="en">
<head>
<meta charset="utf-8">
<title>Radiant Harvest Gathering 2021</title>
<link rel="stylesheet" href="https://fonts.googleapis.com/css2?family=Oswald:wght@400;500;600&family=Comfortaa:wght@400;500&display=swap">
<style>
  :root {
    --page: #ffffff;
    --slate: #3c4749;
    --slate-dark: #2c3536;
    --amber: #f5a51c;
    --white: #ffffff;
    --mist: #d4d6d4;
    --photo-light: #ddd6ca;
    --photo-warm: #b99a76;
  }
  * { margin: 0; padding: 0; box-sizing: border-box; }
  html, body { width: 1200px; height: 1000px; overflow: hidden; background: var(--page); }
  .canvas { position: relative; width: 1200px; height: 1000px; }
  .flyer {
    position: absolute; left: 245px; top: 0; width: 710px; height: 1000px;
    background: radial-gradient(ellipse at 60% 40%, #46524f 0%, var(--slate) 55%, var(--slate-dark) 100%);
    overflow: hidden;
  }
  .photo-area {
    position: absolute; left: 0; top: 150px; width: 335px; height: 705px;
    background: linear-gradient(100deg, var(--photo-light) 0%, #d3c9b9 55%, var(--photo-warm) 100%);
  }
  .brand-badge {
    position: absolute; left: 475px; top: 34px; width: 105px; height: 105px;
    border-radius: 50%; background: var(--white);
    display: flex; align-items: center; justify-content: center;
    font-family: "Oswald", sans-serif; font-weight: 500; font-size: 19px;
    color: var(--slate-dark); letter-spacing: 1px;
  }
  .tagline {
    position: absolute; left: 410px; width: 235px; top: 170px; text-align: center;
    font-family: "Oswald", sans-serif; font-weight: 500;
    font-size: 15.5px; line-height: 19px; color: var(--mist); letter-spacing: 0.3px;
  }
  .proclamation {
    position: absolute; left: 412px; top: 276px;
    font-family: "Oswald", sans-serif; font-weight: 600; text-transform: uppercase;
  }
  .proclamation .line-accent { display: block; font-size: 43px; line-height: 48px; color: var(--amber); letter-spacing: -1px; }
  .proclamation .line-main { display: flex; align-items: flex-end; font-size: 52px; line-height: 54px; color: var(--white); letter-spacing: 0.5px; }
  .chapel-icon { width: 58px; height: 66px; margin-left: 4px; margin-bottom: 6px; }
  .event-title {
    position: absolute; left: 380px; width: 295px; top: 440px; text-align: center;
    font-family: "Oswald", sans-serif; font-weight: 500; text-transform: uppercase;
  }
  .event-title .title-top { display: block; font-size: 31px; line-height: 38px; color: var(--mist); }
  .event-title .title-bottom { display: block; font-size: 46px; line-height: 54px; font-weight: 600; color: var(--amber); }
  .rule { position: absolute; left: 432px; width: 192px; height: 4px; background: var(--white); border-radius: 2px; }
  .rule.upper { top: 596px; }
  .rule.lower { top: 810px; }
  .details {
    position: absolute; left: 418px; width: 220px; top: 624px; text-align: center;
    font-family: "Comfortaa", sans-serif; font-size: 16.5px; line-height: 28px; color: var(--mist);
  }
  .contact {
    position: absolute; left: 410px; width: 235px; top: 857px; text-align: center;
    font-family: "Comfortaa", sans-serif; font-size: 12.5px; line-height: 20px; color: var(--white);
  }
</style>
</head>
<body>
<div class="canvas">
  <section class="flyer">
    <div class="photo-area" role="img" aria-label="Photograph of an open Bible at the Psalms lying on a dark stone surface"></div>

    <div class="brand-badge">QUVELLO</div>

    <p class="tagline">A ONE DAY<br>PRAYER RETREAT.</p>

    <h2 class="proclamation">
      <span class="line-accent">Jesus Chris</span>
      <span class="line-main">Is Lord
        <svg class="chapel-icon" viewBox="0 0 58 66" aria-hidden="true">
          <rect x="26.5" y="0" width="5" height="20" fill="#fff"/>
          <rect x="21" y="5" width="16" height="5" fill="#fff"/>
          <polygon points="29,18 50,38 46,38 46,66 12,66 12,38 8,38" fill="#fff"/>
          <polygon points="29,16 58,44 53,44 29,21 5,44 0,44" fill="#fff"/>
          <rect x="25" y="50" width="8" height="16" fill="#3c4749"/>
          <circle cx="29" cy="38" r="3.5" fill="#3c4749"/>
        </svg>
      </span>
    </h2>

    <h1 class="event-title">
      <span class="title-top">Radiant Harvest</span>
      <span class="title-bottom">Gathering</span>
    </h1>

    <div class="rule upper"></div>
    <p class="details">
      Tuesday July 2nd, 2021<br>
      11:00AM - 7:00PM<br>
      Bellmore Hotel, 4817 Wexley Avenue, Portland, Maine 04109 (Room: Tamarind)
    </p>
    <div class="rule lower"></div>

    <p class="contact">
      www.quvello.org<br>
      207 555 0148<br>
      contact@brookmeadow.org
    </p>
  </section>
</div>
</body>
</html>
```